Business card for Full Stable Care Vandorpe

I would like to have me designed an professional business card with my existing logo for my company called : full stable care vandorpe gcv.
I prefer a two sided business card with on the back side only the horses head and the website : fscvandorpe-example.eu
Only one colour shouldbe all right.
The logo must appear in a nic professional way on the business card.

Other suggestion are welcome.

All copy wrights must be released by the designer after we have selected a final design.

Target Market(s)

Equestrian businesses

Industry/Entity Type

Business

Contact Information for Business Card

Laurent Vandorpe
Title: zaakvoerder
Full Stable Care Vandorpe GCV
Molkenweg 47
B - 2870 Hoevedonk
België
Phone: + 32 491 68 27 04
Mail: laurent@fscvandorpe-example.eu

Font styles to use
Serif

Requirements
Must have
• My own logo
• See attached files
• Website: fscvandorpe-example.eu

```html
<!DOCTYPE html>
<html lang="nl">
<head>
<meta charset="utf-8">
<title>Full Stable Care Vandorpe – Business Card</title>
<link rel="stylesheet" href="https://fonts.googleapis.com/css2?family=Noto+Serif:wght@400;700&display=swap">
<style>
  :root {
    --page: #2b2b2d;
    --card: #050505;
    --ink: #ffffff;
    --muted: #d9d9d9;
    --edge: #bdbdbd;
    --tab: #ffffff;
    --tab-ink: #111111;
  }
  * { box-sizing: border-box; margin: 0; padding: 0; }
  html, body {
    width: 1200px; height: 900px; overflow: hidden;
    background: var(--page);
    font-family: "Noto Serif", Georgia, serif;
  }
  .stage { position: relative; width: 1200px; height: 900px; }
  .card {
    position: absolute; width: 620px; height: 340px;
    left: 290px; background: var(--card);
    border-radius: 22px; overflow: hidden; color: var(--ink);
  }
  .card--back { top: 90px; }
  .card--front { top: 470px; }
  .card__shapes { position: absolute; inset: 0; }

  /* back */
  .back-mark {
    position: absolute; left: 0; right: 0; top: 62px;
    display: flex; flex-direction: column; align-items: center; gap: 14px;
  }
  .back-mark__dot {
    width: 92px; height: 92px; border-radius: 50%;
    background: linear-gradient(135deg, #e6e6e6, #6e6e6e);
  }
  .back-mark__name {
    font-size: 22px; font-weight: 700; letter-spacing: 1px; color: var(--muted);
  }
  .back-url {
    position: absolute; left: 34px; bottom: 14px;
    font-size: 15px; color: var(--tab-ink); font-weight: 700;
  }

  /* front */
  .brand {
    position: absolute; left: 34px; top: 48px;
    display: flex; align-items: center; gap: 12px;
  }
  .brand__dot { width: 26px; height: 26px; border-radius: 50%; background: var(--ink); }
  .brand__name { font-size: 24px; font-weight: 700; line-height: 1.1; color: var(--ink); }
  .person { position: absolute; right: 34px; top: 44px; text-align: right; }
  .person__name { font-size: 21px; font-weight: 700; padding-bottom: 4px; border-bottom: 1px solid var(--ink); }
  .person__title { font-size: 13px; margin-top: 4px; }
  .person__address { font-size: 13px; margin-top: 14px; line-height: 1.45; }
  .contact {
    position: absolute; left: 34px; top: 208px; width: 300px;
    border-top: 1px solid var(--muted); padding-top: 10px;
    list-style: none;
  }
  .contact li {
    display: flex; align-items: center; gap: 10px;
    font-size: 13.5px; line-height: 1.55;
  }
  .contact svg { width: 11px; height: 11px; flex: none; }
</style>
</head>
<body>
<main class="stage">

  <section class="card card--back" aria-label="Achterkant visitekaartje">
    <svg class="card__shapes" viewBox="0 0 620 340" aria-hidden="true">
      <polygon points="300,328 620,328 620,340 300,340" fill="var(--edge)"/>
      <polygon points="0,340 0,294 262,294 292,270 320,270 320,340" fill="var(--tab)"/>
    </svg>
    <div class="back-mark">
      <span class="back-mark__dot"></span>
      <span class="back-mark__name">Full Stable Care Vandorpe</span>
    </div>
    <p class="back-url">www.fscvandorpe-example.eu</p>
  </section>

  <section class="card card--front" aria-label="Voorkant visitekaartje">
    <svg class="card__shapes" viewBox="0 0 620 340" aria-hidden="true">
      <polygon points="0,340 0,320 620,320 620,340" fill="var(--edge)"/>
      <polygon points="440,290 465,236 620,236 620,290" fill="var(--tab)"/>
    </svg>

    <div class="brand">
      <span class="brand__dot"></span>
      <span class="brand__name">Full Stable Care<br>Vandorpe</span>
    </div>

    <div class="person">
      <p class="person__name">Laurent Vandorpe</p>
      <p class="person__title">Zaakvoerder</p>
      <p class="person__address">Molkenweg 47<br>B - 2870 Hoevedonk België</p>
    </div>

    <ul class="contact">
      <li>
        <svg viewBox="0 0 24 24" fill="var(--ink)"><path d="M6.6 10.8a15 15 0 0 0 6.6 6.6l2.2-2.2c.3-.3.7-.4 1-.2 1.1.4 2.3.6 3.6.6.6 0 1 .4 1 1V20c0 .6-.4 1-1 1A17 17 0 0 1 3 4c0-.6.4-1 1-1h3.5c.6 0 1 .4 1 1 0 1.3.2 2.5.6 3.6.1.3 0 .7-.2 1z"/></svg>
        + 32 491 68 27 04
      </li>
      <li>
        <svg viewBox="0 0 24 24" fill="none" stroke="var(--ink)" stroke-width="2"><rect x="3" y="5" width="18" height="14" rx="1"/><path d="M3 6l9 7 9-7"/></svg>
        laurent@fscvandorpe-example.eu
      </li>
      <li>
        <svg viewBox="0 0 24 24" fill="none" stroke="var(--ink)" stroke-width="2"><circle cx="12" cy="12" r="9"/><path d="M3 12h18M12 3c3 3 3 15 0 18M12 3c-3 3-3 15 0 18"/></svg>
        www.fscvandorpe-example.eu
      </li>
    </ul>
  </section>

</main>
</body>
</html>
```